New design of old website

We need a new design of our domain name reseller website.

quilanorte.com

we would also like new design for Logo and all.

the site will be in English and portuguesse,

Industry/Entity Type

Domain

```html
<!DOCTYPE html>
<html lang="en">
<head>
<meta charset="utf-8">
<title>Quilanorte – Domain Reseller</title>
<link href="https://fonts.googleapis.com/css2?family=Rokkitt:wght@400;500&family=Open+Sans:ital,wght@0,400;0,600;0,700;1,400&family=Arimo:wght@400;700&display=swap" rel="stylesheet">
<style>
:root{
  --navy:#064d80;
  --bar-top:#0b679f;
  --blue:#1a6aa8;
  --sky:#1996d6;
  --orange:#f07a10;
  --orange-light:#ffb324;
  --ink:#1d4563;
  --brown:#4a3b2a;
  --text:#333;
  --grey:#8a8a8a;
  --line:#c9c9c9;
  --white:#fff;
}
*{box-sizing:border-box;margin:0;padding:0}
html,body{width:1200px;height:1000px;overflow:hidden;background:var(--white)}
body{position:relative;font-family:"Arimo",Arial,sans-serif;color:var(--text)}
.abs{position:absolute}

/* top bar */
.topbar{left:0;top:0;width:1200px;height:38px;background:linear-gradient(var(--bar-top),var(--navy));border-bottom:2px solid #04416c}
.topbar span{position:absolute;top:12px;font:700 12px "Arimo",Arial,sans-serif;color:var(--white)}

/* header */
.header{left:0;top:38px;width:1200px;height:175px;background:linear-gradient(#fff 70%,#f1f1f1)}
.brand{left:98px;top:80px;display:flex;align-items:center;gap:10px;font:700 40px "Open Sans",sans-serif;color:var(--navy)}
.brand i{width:34px;height:34px;border-radius:50%;background:var(--orange);display:block}
.phone-num{left:565px;top:90px;font:700 20px "Arimo",Arial,sans-serif;color:var(--orange)}
.phone-hours{left:570px;top:114px;font:11px "Arimo",Arial,sans-serif;color:#222}
.top-search{left:788px;top:91px;width:268px;height:37px;border:1px solid #ddd;border-right:none;border-radius:3px 0 0 3px;padding:10px 12px;font:14px "Arimo",Arial,sans-serif;color:#999;background:#fff}
.top-search-btn{left:1056px;top:91px;width:40px;height:37px;background:linear-gradient(#ffb63a,#f39a0a);border-radius:0 3px 3px 0}
.social{top:158px;width:42px;height:42px;border-radius:50%;box-shadow:0 2px 3px rgba(0,0,0,.35)}
.nav{left:97px;top:178px;display:flex;height:33px}
.nav a{display:block;padding:8px 0 0;font:14px "Arimo",Arial,sans-serif;color:var(--blue);text-decoration:none;border-left:1px dotted #6a8fb0;text-align:center}
.nav a:last-child{border-right:1px dotted #6a8fb0}

/* hero */
.hero{left:0;top:213px;width:1200px;height:522px;background:radial-gradient(ellipse 620px 420px at 600px 240px,#f2cf95 0%,#ebb868 45%,#e88f28 85%,#e5801a 100%)}
.hero h1{left:0;width:1200px;top:240px;text-align:center;font:500 40px "Rokkitt",serif;color:var(--ink)}
.hero h2{left:0;width:1200px;top:292px;text-align:center;font:400 29px "Rokkitt",serif;color:var(--brown)}
.card{top:369px;width:311px;height:176px;background:#fff;border-top:4px solid var(--blue);border-radius:3px;box-shadow:0 10px 10px -4px rgba(60,30,0,.55)}
.card-title{left:0;top:12px;width:100%;text-align:center;font:600 23px "Open Sans",sans-serif;color:#444}
.card-title b{color:var(--blue);font-size:18px;margin:0 14px;vertical-align:2px}
.card-rule{left:12px;right:13px;top:43px;border-top:1px dashed #b5b5b5}
.card-art{left:18px;top:66px;width:90px;height:90px;border-radius:8px}
.card-lead{left:141px;top:72px;font:14px "Arimo",Arial,sans-serif;color:#0d4f85}
.card-price{left:140px;top:88px;font:34px "Arimo",Arial,sans-serif;color:var(--orange)}
.card-more{left:145px;top:141px;font:700 12px "Arimo",Arial,sans-serif;color:#222}
.reseller-btn{left:450px;top:580px;width:295px;height:51px;border-radius:4px;background:linear-gradient(#1e78b5,#0b4f84);border:1px solid #0a3e66;box-shadow:inset 0 1px 0 rgba(255,255,255,.35);text-align:center;font:500 28px/48px "Rokkitt",serif;color:#fff}
.hero-call{left:0;width:1200px;top:649px;text-align:center;font:16px "Arimo",Arial,sans-serif;color:#333}

/* domain search */
.domain-box{left:99px;top:681px;width:995px;height:116px;background:var(--sky);border-radius:3px}
.domain-box h3{left:0;width:100%;top:10px;text-align:center;font:600 24px "Open Sans",sans-serif;color:#fff}
.domain-input{left:103px;top:56px;width:634px;height:42px;background:#fff;border-radius:4px;box-shadow:inset 0 2px 3px rgba(0,0,0,.15)}
.domain-input span{position:absolute;left:16px;top:12px;font:16px "Arimo",Arial,sans-serif;color:#999}
.domain-tld{position:absolute;left:539px;top:0;width:95px;height:42px;border-left:1px solid #ddd;padding:12px 0 0 18px;font:16px "Arimo",Arial,sans-serif;color:#999}
.domain-btn{left:749px;top:55px;width:133px;height:44px;border-radius:4px;background:linear-gradient(#ffc43c,#f39a0a);border:1px solid #d98200;text-align:center;font:500 25px/40px "Rokkitt",serif;color:#fff;text-shadow:0 1px 1px rgba(0,0,0,.3)}

/* why */
.why-title{left:98px;top:819px;font:26px "Arimo",Arial,sans-serif;color:#444}
.why-sub{left:101px;top:852px;font:18px "Arimo",Arial,sans-serif;color:var(--orange)}
.why-rule{left:98px;top:882px;width:692px;border-top:1px dashed #aaa}
.why-text{left:102px;top:901px;width:692px;font:14px/21px "Arimo",Arial,sans-serif;color:var(--grey)}
.aside{left:822px;top:810px;width:280px;height:190px;border-left:1px solid #e3e3e3}
.aside h4{position:absolute;left:17px;top:12px;font:italic 14px "Arimo",Arial,sans-serif;color:var(--orange)}
.aside ul{position:absolute;left:17px;top:40px;width:250px;list-style:none}
.aside li{position:relative;padding-left:22px;margin-bottom:16px;font:12px/18px "Arimo",Arial,sans-serif;color:var(--grey)}
.aside li svg{position:absolute;left:0;top:4px}
</style>
</head>
<body>

<div class="abs topbar">
  <span style="left:104px">My Account | My Reports | Account Settings</span>
  <span style="left:708px">★ Special Offers | Help Center</span>
  <span style="left:984px">Login | Register</span>
  <svg class="abs" style="left:1080px;top:11px" width="18" height="15" viewBox="0 0 18 15"><circle cx="7" cy="4" r="3.5" fill="#fff"/><path d="M0 15c0-5 3-7 7-7s7 2 7 7z" fill="#fff"/><circle cx="13" cy="3.5" r="2.8" fill="#fff"/><path d="M12 7c3 0 6 2 6 6h-3c0-2-1-4-3-6z" fill="#fff"/></svg>
</div>

<div class="abs header">
</div>
<div class="abs brand"><i></i>Quilanorte</div>
<svg class="abs" style="left:537px;top:96px" width="20" height="30" viewBox="0 0 20 30"><path d="M5 1c-3 1-5 4-4 9 1 7 5 14 10 18 2 2 5 1 7-1l-4-6c-1 0-2 1-3 1-2-2-4-6-4-9 1-1 2-1 2-2L6 1z" fill="#1a6aa8"/></svg>
<div class="abs phone-num">1 (555) 010-2040</div>
<div class="abs phone-hours">Mon-Fri 12pm-6pm, Sat 12pm-4pm</div>
<div class="abs top-search">Register A Domain</div>
<div class="abs top-search-btn">
  <svg class="abs" style="left:13px;top:11px" width="14" height="14" viewBox="0 0 14 14"><circle cx="6" cy="6" r="4" fill="none" stroke="#fff" stroke-width="2"/><path d="M9 9l4 4" stroke="#fff" stroke-width="2.2"/></svg>
</div>
<div class="abs social" style="left:999px;background:#263f8c" role="img" aria-label="Social network link"></div>
<div class="abs social" style="left:1050px;background:#2fb3e0" role="img" aria-label="Social network link"></div>
<nav class="abs nav">
  <a style="width:71px">Home</a>
  <a style="width:112px">Why Quilanorte</a>
  <a style="width:94px">Products</a>
  <a style="width:93px">Services</a>
  <a style="width:90px">Reseller</a>
  <a style="width:90px">Contact</a>
  <a style="width:91px">My Cart</a>
</nav>

<div class="abs hero"></div>
<h1 class="abs" style="left:0;width:1200px;top:240px;text-align:center;font:500 40px 'Rokkitt',serif;color:var(--ink)">Earn more when you sell online services with Quilanorte</h1>
<h2 class="abs" style="left:0;width:1200px;top:292px;text-align:center;font:400 29px 'Rokkitt',serif;color:var(--brown)">We offer feature packed services at the best prices</h2>

<div class="abs card" style="left:101px">
  <div class="abs card-title"><b>★</b>Domain Names<b>★</b></div>
  <div class="abs card-rule"></div>
  <div class="abs card-art" role="img" aria-label="Globe illustration" style="border-radius:50%;background:radial-gradient(circle at 35% 35%,#8fd4ff,#1f7fd0 60%,#0b4f9a)"></div>
  <div class="abs card-lead">On SALE as low as</div>
  <div class="abs card-price">$9.00/yr</div>
  <div class="abs card-more">Learn More</div>
</div>
<div class="abs card" style="left:442px">
  <div class="abs card-title"><b>★</b>Web Hosting<b>★</b></div>
  <div class="abs card-rule"></div>
  <div class="abs card-art" role="img" aria-label="Server rack illustration" style="background:linear-gradient(#e4e4e4,#a9a9a9)"></div>
  <div class="abs card-lead">Starting as low as</div>
  <div class="abs card-price">$4.88/mo</div>
  <div class="abs card-more">Learn More</div>
</div>
<div class="abs card" style="left:781px">
  <div class="abs card-title"><b>★</b>SSL Certificates<b>★</b></div>
  <div class="abs card-rule"></div>
  <div class="abs card-art" role="img" aria-label="Padlock illustration" style="background:linear-gradient(#e8e8e8,#9a9a9a)"></div>
  <div class="abs card-lead">Starting as low as</div>
  <div class="abs card-price">$9.95/yr</div>
  <div class="abs card-more">Learn More</div>
</div>

<div class="abs reseller-btn">Become a Reseller</div>
<div class="abs hero-call">Have Questions? Give us a Call at 1 (555) 010-2040</div>

<div class="abs domain-box">
  <h3 class="abs" style="left:0;width:100%;top:10px;text-align:center;font:600 24px 'Open Sans',sans-serif;color:#fff">Just want a domain name?</h3>
  <div class="abs domain-input"><span>Search A Domain Name</span>
    <div class="domain-tld">.com
      <svg class="abs" style="left:66px;top:17px" width="13" height="8" viewBox="0 0 13 8"><path d="M0 0h13L6.5 8z" fill="#999"/></svg>
    </div>
  </div>
  <div class="abs domain-btn">Search</div>
</div>

<div class="abs why-title">Why Quilanorte?</div>
<div class="abs why-sub">Give your customers a choice of 250 Top Level Domains (TLDs)</div>
<div class="abs why-rule"></div>
<p class="abs why-text">Quilanorte is mainly focused the the latin american marked. Today Quilanorte is the fastest growing .br registrar and today many of the world’s largest registrars are using Quilanic to register .br domain with or without local pres­ent. With the unique QuilaNIC registration engine, you can offer your customers more than 200 top-level domains (TLDs).</p>

<aside class="abs aside">
  <h4>Why More People Use Quilanorte?</h4>
  <ul>
    <li><svg width="10" height="9" viewBox="0 0 10 9"><path d="M1 5l3 3 5-7" fill="none" stroke="#aaa" stroke-width="2"/></svg>We have gone further than anyone else in automating and optimizing the processing of ccTLDs.</li>
    <li><svg width="10" height="9" viewBox="0 0 10 9"><path d="M1 5l3 3 5-7" fill="none" stroke="#aaa" stroke-width="2"/></svg>This ensures fast fulfillment and consistent order tracking and makes registering and transferring ccTLDs as quick and reliable as dealing with global domains.</li>
  </ul>
</aside>

</body>
</html>
```